Lantern Hill Publicity is a new boutique Press Office with a small roster of well-chosen clients across an array of disciplines; from Art and Technology to Restaurants and Fashion. Based in Greenpoint Brooklyn, Lantern Hill Publicity achieves outstanding results through hard work, tenacity, efficiency and a sense of humor. We need a simple, versatile and classic design. We would like each side of the card to be white text on a black background.

Boutique

```html
<!DOCTYPE html>
<html lang="en">
<head>
<meta charset="utf-8">
<title>Lantern Hill Publicity – Business Card</title>
<link rel="stylesheet" href="https://fonts.googleapis.com/css2?family=Montserrat:wght@400;500;600;700&display=swap">
<style>
  :root {
    --backdrop: #e7e4df;
    --card: #1b1b1b;
    --ink: #ffffff;
    --ink-soft: #e6e6e6;
  }
  html, body {
    margin: 0;
    padding: 0;
    width: 1200px;
    height: 1000px;
    overflow: hidden;
    background: var(--backdrop);
    font-family: "Montserrat", Arial, sans-serif;
    color: var(--ink);
  }
  .canvas {
    position: relative;
    width: 1200px;
    height: 1000px;
  }
  .card {
    position: absolute;
    left: 267px;
    width: 665px;
    height: 397px;
    background: var(--card);
    box-shadow: 0 3px 10px rgba(0,0,0,0.25);
    overflow: hidden;
  }
  .card--front { top: 74px; }
  .card--back { top: 533px; }

  .brand-name {
    margin: 0;
    font-weight: 500;
    color: var(--ink);
    text-transform: uppercase;
    letter-spacing: 0.18em;
    white-space: nowrap;
  }
  .card--front .brand-name {
    position: absolute;
    left: 32px;
    top: 108px;
    font-size: 19px;
  }

  .contact-person {
    position: absolute;
    left: 32px;
    top: 214px;
  }
  .contact-person__name {
    margin: 0;
    font-size: 17px;
    font-weight: 700;
    letter-spacing: 0.01em;
    text-transform: uppercase;
  }
  .contact-person__role {
    margin: 3px 0 0;
    font-size: 14px;
    font-weight: 400;
    color: var(--ink-soft);
  }

  .contact-list {
    position: absolute;
    left: 32px;
    top: 280px;
    margin: 0;
    padding: 0;
    list-style: none;
    font-size: 14px;
    color: var(--ink-soft);
  }
  .contact-list li {
    display: flex;
    align-items: center;
    height: 21px;
  }
  .contact-list .icon {
    width: 14px;
    height: 14px;
    margin-right: 7px;
    fill: var(--ink-soft);
  }
  .contact-list .address {
    margin-top: 6px;
  }

  .card--back .brand-name {
    position: absolute;
    left: 0;
    right: 0;
    top: 188px;
    text-align: center;
    font-size: 24px;
  }
</style>
</head>
<body>
<main class="canvas">

  <section class="card card--front" aria-label="Card front">
    <p class="brand-name">Lantern Hill Publicity</p>

    <div class="contact-person">
      <p class="contact-person__name">Marion Castell</p>
      <p class="contact-person__role">Managing Director</p>
    </div>

    <ul class="contact-list">
      <li>
        <svg class="icon" viewBox="0 0 16 16" aria-hidden="true">
          <path d="M2 6c0-2 2.5-3 6-3s6 1 6 3v1.2h-3V5.8C10 5.3 9 5 8 5s-2 .3-2 .8v1.4H2z"/>
          <path d="M4 8h8l1.5 5h-11z"/>
        </svg>
        + 000 000 0000 EXT 1
      </li>
      <li>
        <svg class="icon" viewBox="0 0 16 16" aria-hidden="true">
          <path d="M1 3.5h14v9H1z M2 4.5l6 4.5 6-4.5"/>
          <path d="M1.5 4l6.5 5 6.5-5" fill="none" stroke="#1b1b1b" stroke-width="1"/>
        </svg>
        info@lanternhillpublicity.com
      </li>
      <li>
        <svg class="icon" viewBox="0 0 16 16" aria-hidden="true">
          <circle cx="7.5" cy="7.5" r="6" fill="none" stroke="#e6e6e6" stroke-width="1.6"/>
          <path d="M1.5 7.5h12M7.5 1.5c-2.5 3-2.5 9 0 12M7.5 1.5c2.5 3 2.5 9 0 12" fill="none" stroke="#e6e6e6" stroke-width="1.1"/>
          <path d="M9 9l6 2.2-2.4 1 -1 2.4z"/>
        </svg>
        www.lanternhillpublicity.com
      </li>
      <li class="address">418 Alder Street New York, NY 10022</li>
    </ul>
  </section>

  <section class="card card--back" aria-label="Card back">
    <p class="brand-name">Lantern Hill Publicity</p>
  </section>

</main>
</body>
</html>
```